Tolvik Hearthline Website Images

We manufacture electric fireplaces and require images of our new product in various sizes.
We have 5 sizes of fireplace. A 36", 42", 50", 72" and a 100". However, the only image we currently have is for a 60", but need these same images to show the product in 36", 42", 50", 72" and 100". Therefore, a scale needs to be made so the images look different for each size of fireplace. The photos we already have show the fire with its different coloured flames.
We require:
1. Close up image showing all the different flame colours. Attached is an example of how it needs to look, but with our colours as per our images (EXAMPLE_flamecolourscloseup)
2. I have uploaded the images (S1-S16) which need to be scaled to show all sizes of the fireplace (36", 42", 50", 72", 100").
3. Image S12 with the dimensions of each size. Example attached (EXAMPLE_fireplacedimensions). Dimensions are as follows:
36" - 914 mm x 140 mm x 430 mm. 16.7 kg.
42" - 1060 mm x 140 mm x 430 mm. 19.5 kg.
50" - 1270 mm x 140 mm x 430 mm. 22.6 kg.
72" - 1829 mm x 140 mm x 430 mm. 35.5 kg.
100" - 2540 mm x 140 mm x 430 mm. 49.3 kg.
4. We also require the product highlights to be added like the attached example (EXAMPLE_fireplacehighlights) but with the new fireplace model image (S12).
5. We also require image and writing attached (EXAMPLE_heatoutput) with our image S12.
6. We also require image (new_purple) to be photoshopped with our new fireplace (image S11-S16).
Logos etc all attached too.
I hope this makes sense. Any questions, please ask :)

```html
<!DOCTYPE html>
<html lang="en">
<head>
<meta charset="utf-8">
<title>Tolvik Hearthline – Slim Frame</title>
<link rel="stylesheet" href="https://fonts.googleapis.com/css2?family=Lato:wght@400;700&family=Kalam:wght@400&display=swap">
<style>
  :root {
    --bg: #ffffff;
    --frame: #2b2b2d;
    --frame-inner: #121212;
    --glass: #0a0605;
    --vent: #3a3a3c;
    --inlet: #1db6e3;
    --outlet: #ef7a30;
    --ink: #1d1d1f;
    --dim-line: #222222;
    --panel-icon: #cfcfcf;
    --panel-power: #e2452b;
  }
  html, body {
    margin: 0;
    padding: 0;
    width: 1200px;
    height: 854px;
    overflow: hidden;
    background: var(--bg);
  }
  .product-sheet {
    display: block;
    width: 1200px;
    height: 854px;
  }
  .airflow-label {
    font-family: "Kalam", cursive;
    font-size: 14px;
    fill: var(--ink);
  }
  .caption {
    font-family: "Lato", sans-serif;
    font-size: 18.5px;
    fill: var(--ink);
  }
  .dimension-label {
    font-family: "Lato", sans-serif;
    font-size: 13.5px;
    fill: var(--ink);
  }
  .inlet-arrow { stroke: var(--inlet); fill: none; stroke-width: 2.2; stroke-linecap: round; }
  .outlet-arrow { stroke: var(--outlet); fill: none; stroke-width: 2.2; stroke-linecap: round; }
  .dim-line { stroke: var(--dim-line); stroke-width: 0.9; fill: none; }
</style>
</head>
<body>
<svg class="product-sheet" viewBox="0 0 1000 711.67" xmlns="http://www.w3.org/2000/svg">
  <defs>
    <marker id="head-inlet" viewBox="0 0 10 10" refX="7" refY="5" markerWidth="6" markerHeight="6" orient="auto">
      <path d="M1 1 L8 5 L1 9" fill="none" stroke="#1db6e3" stroke-width="1.6" stroke-linecap="round" stroke-linejoin="round"/>
    </marker>
    <marker id="head-outlet" viewBox="0 0 10 10" refX="7" refY="5" markerWidth="6" markerHeight="6" orient="auto">
      <path d="M1 1 L8 5 L1 9" fill="none" stroke="#ef7a30" stroke-width="1.6" stroke-linecap="round" stroke-linejoin="round"/>
    </marker>
    <marker id="head-dim" viewBox="0 0 10 10" refX="9" refY="5" markerWidth="7" markerHeight="7" orient="auto">
      <path d="M0 2 L9 5 L0 8 Z" fill="#222"/>
    </marker>
    <linearGradient id="flame-tones" x1="0" y1="0" x2="0" y2="1">
      <stop offset="0" stop-color="#0a0605"/>
      <stop offset="0.28" stop-color="#1a0703"/>
      <stop offset="0.5" stop-color="#8a2a0a"/>
      <stop offset="0.72" stop-color="#e8631c"/>
      <stop offset="0.9" stop-color="#ffb347"/>
      <stop offset="1" stop-color="#d9743a"/>
    </linearGradient>
    <radialGradient id="floor-shadow" cx="0.5" cy="0.3" r="0.6">
      <stop offset="0" stop-color="#000" stop-opacity="0.22"/>
      <stop offset="1" stop-color="#000" stop-opacity="0"/>
    </radialGradient>
  </defs>

  <!-- Floor shadow -->
  <ellipse cx="499" cy="440" rx="350" ry="12" fill="url(#floor-shadow)"/>

  <!-- Fireplace unit -->
  <g class="fireplace">
    <rect class="frame" x="158" y="258" width="682" height="178" fill="var(--frame)"/>
    <rect class="frame-inner" x="168" y="266" width="662" height="162" fill="var(--frame-inner)"/>
    <rect class="top-vent" x="170" y="269" width="658" height="11" fill="var(--vent)"/>
    <rect class="vent-slots" x="170" y="272" width="658" height="5" fill="#262628"/>
    <rect class="glass" x="180" y="288" width="640" height="124" fill="var(--glass)"/>
    <g role="img" aria-label="Orange and yellow flames rising over a bed of glowing crystal embers">
      <rect x="180" y="288" width="640" height="124" fill="url(#flame-tones)"/>
    </g>
    <rect class="control-strip" x="180" y="412" width="640" height="14" fill="#0c0c0c"/>
    <g class="control-panel">
      <rect x="745" y="416" width="2" height="5" fill="var(--outlet)"/>
      <rect x="748" y="416" width="2" height="5" fill="var(--outlet)"/>
      <rect x="757" y="416" width="5" height="5" fill="var(--panel-icon)"/>
      <rect x="767" y="416" width="4" height="5" fill="var(--panel-icon)"/>
      <rect x="777" y="416" width="4" height="5" fill="var(--panel-icon)"/>
      <circle cx="790" cy="418.5" r="2.3" fill="var(--panel-icon)"/>
      <circle cx="801" cy="418.5" r="2.3" fill="var(--panel-icon)"/>
      <circle cx="813" cy="418.5" r="2.6" fill="none" stroke="var(--panel-power)" stroke-width="1.1"/>
    </g>
  </g>

  <!-- Airflow labels -->
  <text class="airflow-label" x="202" y="221">Air Inlet</text>
  <text class="airflow-label" x="494" y="221">Air Outlet</text>
  <text class="airflow-label" x="746" y="221">Air Inlet</text>

  <!-- Inlet arrows -->
  <path class="inlet-arrow" d="M206 230 Q238 240 256 270" marker-end="url(#head-inlet)"/>
  <path class="inlet-arrow" d="M253 230 Q285 240 303 270" marker-end="url(#head-inlet)"/>
  <path class="inlet-arrow" d="M746 230 Q713 240 697 270" marker-end="url(#head-inlet)"/>
  <path class="inlet-arrow" d="M794 230 Q761 240 745 270" marker-end="url(#head-inlet)"/>

  <!-- Outlet arrows -->
  <path class="outlet-arrow" d="M444 274 Q478 262 494 235" marker-end="url(#head-outlet)"/>
  <path class="outlet-arrow" d="M492 274 Q526 262 542 235" marker-end="url(#head-outlet)"/>

  <!-- Frame width dimension -->
  <line class="dim-line" x1="818" y1="414" x2="818" y2="462"/>
  <line class="dim-line" x1="840" y1="436" x2="840" y2="462"/>
  <line class="dim-line" x1="795" y1="455" x2="817" y2="455" marker-end="url(#head-dim)"/>
  <line class="dim-line" x1="866" y1="455" x2="841" y2="455" marker-end="url(#head-dim)"/>
  <text class="dimension-label" x="826" y="483" text-anchor="middle">30mm</text>

  <!-- Caption -->
  <text class="caption" x="153" y="483">30mm Wide Slim Frame, Modern and Quality</text>
</svg>
</body>
</html>
```